Mirelo Japanese Restaurant

We just want the japanese sakura background and the menu as below

Side dish :
Edamame $4
Japanese Steam Green Bean
Crab Craw $3 each
With Japanese mayo
Teriyaki Chicken stick $3 each
Chicken stick with home made teriyaki sauce
Tempura Prawns $7
With Japanese mayo
Miso Soup $3
Traditional Japanese soup
Salt and Pepper Calamari $7
With japanese mayo

Main dish:
Gyu Don $12
Bowl of steam rice topped with beef and onion simmered in a mildly sweet sauce.
Teriyaki Don $12
Bowl of steam rice topped with your choice of beef, chicken or pork and with our special Teriyaki sauce.
Vege Don $12
Bowl of steam rice with seasonal Vegetables with the special japanese sweet soy sauce.
Japanese Curry $12,(prawns $14)
Bowl of steam rice with Chicken, pork or prawn with japanese mild curry sauce.
Katsu Don $12
Bowl of steam rice topped with a deep-fried pork cutlet and egg with the japanese special sauce.
Oyako Don $12
Bowl of steam rice topped with chick and egg with japanese special sauce.
Spice Don $12
Bowl of steam rice topped with beef or chicken with japanese spice sauce.
Gingle Don $12
Bowl of steam rice topped with beef or chicken with japanese ginger sauce.
Sushi $3
Roll everyday on seasonal
ingredient.

Japanese-style sweets
Black Sesame Ice cream $4.5
Green tea Ice cream $4.5

Restaurant

```html
<!DOCTYPE html>
<html lang="en">
<head>
<meta charset="utf-8">
<title>Mirelo Japanese Restaurant – Menu</title>
<link rel="stylesheet" href="https://fonts.googleapis.com/css2?family=Mystery+Quest&family=Tinos&display=swap">
<style>
  :root{
    --canvas:#ffffff;
    --header-bg:#f8e9ec;
    --header-edge:#c9b7ba;
    --body-bg:#efd9da;
    --panel:#fd325f;
    --panel-ink:#ffffff;
    --ink:#1a1416;
    --blossom-soft:rgba(255,196,214,.75);
    --blossom-panel:rgba(255,170,196,.7);
  }
  *{box-sizing:border-box;margin:0;padding:0}
  html,body{width:818px;height:1200px;overflow:hidden;background:var(--canvas)}
  .sheet{position:relative;width:818px;height:1200px}
  .page{position:absolute;left:0;width:818px}
  .page--one{top:0;height:572px}
  .page--two{top:624px;height:576px}

  .masthead{position:absolute;left:42px;top:0;width:776px;height:190px;background:var(--header-bg);border:1px solid var(--header-edge);overflow:hidden}
  .masthead__curve{position:absolute;left:0;top:60px;width:600px;height:90px}
  .masthead__name{position:absolute;left:200px;top:12px;font:400 70px/1 "Mystery Quest",cursive;color:var(--ink);letter-spacing:4px}
  .masthead__tagline{position:absolute;left:150px;top:116px;font:400 46px/1 "Mystery Quest",cursive;color:var(--ink)}
  .masthead__scene{position:absolute;right:0;top:0;width:178px;height:188px;border-left:1px solid var(--header-edge);background:linear-gradient(160deg,#fbeef1 0%,#f3c9d5 55%,#d8c6ca 100%)}

  .backdrop{position:absolute;left:6px;width:812px;background:var(--body-bg);overflow:hidden}
  .page--one .backdrop{top:192px;height:380px}
  .page--two .backdrop{top:192px;height:384px}
  .backdrop__blossom{position:absolute;left:230px;top:-60px;width:380px;height:440px;border-radius:50%;background:radial-gradient(ellipse at 50% 45%,var(--blossom-soft) 0%,rgba(255,196,214,.45) 45%,rgba(255,196,214,0) 72%)}

  .panel{position:absolute;background:var(--panel);color:var(--panel-ink);overflow:hidden}
  .panel__art{position:absolute;left:10px;right:10px;top:40px;bottom:0;border-radius:50%;background:radial-gradient(circle,var(--blossom-panel) 0%,rgba(255,170,196,.35) 45%,rgba(255,170,196,0) 72%)}
  .panel__title{position:relative;text-align:center;font:400 42px/1 "Mystery Quest",cursive;padding-top:8px;white-space:nowrap}
  .panel__title--small{font-size:34px;padding-top:12px}
  .panel__icon{position:absolute;width:44px;height:34px;border-radius:50%;background:radial-gradient(circle,#7a9b4a 0%,#e9efe2 75%)}

  .menu{position:relative;list-style:none;padding:10px 8px 0 10px;font-family:"Tinos",serif}
  .menu__row{display:flex;align-items:baseline;font-size:16px;line-height:1.05}
  .menu__leader{flex:1;border-bottom:2px dotted var(--panel-ink);margin:0 2px 4px}
  .menu__note{font-size:12px;line-height:1.1;padding-left:2px;margin-bottom:5px}
  .menu--compact .menu__row{line-height:1}
  .menu--compact .menu__note{font-size:11.5px;margin-bottom:3px}
  .menu--sweets{padding-top:18px}
  .menu--sweets .menu__row{margin-bottom:12px}

  .panel--side{left:48px;top:235px;width:328px;height:294px}
  .panel--main{left:444px;top:235px;width:330px;height:294px}
  .panel--main2{left:44px;top:235px;width:328px;height:320px}
  .panel--sweets{left:442px;top:235px;width:328px;height:320px}
</style>
</head>
<body>
<div class="sheet">

  <section class="page page--one">
    <header class="masthead">
      <svg class="masthead__curve" viewBox="0 0 600 90" aria-hidden="true"><path d="M60 40 C180 70 260 60 360 50 S540 30 600 28" fill="none" stroke="#2b2326" stroke-width="2"/></svg>
      <div class="masthead__name">MIRELO</div>
      <div class="masthead__tagline">Japanese Restaurant</div>
      <div class="masthead__scene" role="img" aria-label="Ink painting of a blossoming cherry tree beside a snowy mountain"></div>
    </header>
    <div class="backdrop"><div class="backdrop__blossom" role="img" aria-label="Large faint sakura blossom background"></div></div>

    <article class="panel panel--side">
      <div class="panel__art" role="img" aria-label="Pink sakura flower illustration"></div>
      <h2 class="panel__title">Side Dish</h2>
      <ul class="menu">
        <li class="menu__row">Edamame<span class="menu__leader"></span>$4</li>
        <li class="menu__note">(Japanese steam green bean)</li>
        <li class="menu__row">Crab Claw<span class="menu__leader"></span>$3</li>
        <li class="menu__note">(with Japanese mayo)</li>
        <li class="menu__row">Teriyaki Chicken Stick<span class="menu__leader"></span>$3 ea</li>
        <li class="menu__note">(chicken with home made teriyaki sauce)</li>
        <li class="menu__row">Tempura Prawns<span class="menu__leader"></span>$7</li>
        <li class="menu__note">(with Japanese mayo)</li>
        <li class="menu__row">Miso Soup<span class="menu__leader"></span>$3</li>
        <li class="menu__note">(Traditional Japanese Soup)</li>
        <li class="menu__row">Salt &amp; Pepper Calamari<span class="menu__leader"></span>$7</li>
        <li class="menu__note">(with Japanese mayo)</li>
      </ul>
    </article>

    <article class="panel panel--main">
      <div class="panel__art" role="img" aria-label="Pink sakura flower illustration"></div>
      <div class="panel__icon" style="left:-4px;top:6px" role="img" aria-label="Bowl of edamame"></div>
      <h2 class="panel__title">Main Dish</h2>
      <ul class="menu">
        <li class="menu__row">GyuDon<span class="menu__leader"></span>$12</li>
        <li class="menu__note">(bowl of steamed rice toped with beef<br>&nbsp;&amp; onion simmered in a mildly sweet<br>&nbsp;sauce)</li>
        <li class="menu__row">TeriyakiDon<span class="menu__leader"></span>$12</li>
        <li class="menu__note">(bowl of steamed rice topped with your<br>&nbsp;choice of beef, chicken or pork &amp; with<br>&nbsp;our special teriyaki sauce)</li>
        <li class="menu__row">VegeDon<span class="menu__leader"></span>$12</li>
        <li class="menu__note">(bowl of steamed rice with seasonal<br>&nbsp;vegetables with the special<br>&nbsp;Japanese sweet soya sauce)</li>
      </ul>
    </article>
  </section>

  <section class="page page--two">
    <header class="masthead">
      <svg class="masthead__curve" viewBox="0 0 600 90" aria-hidden="true"><path d="M60 40 C180 70 260 60 360 50 S540 30 600 28" fill="none" stroke="#2b2326" stroke-width="2"/></svg>
      <div class="masthead__name">MIRELO</div>
      <div class="masthead__tagline">Japanese Restaurant</div>
      <div class="masthead__scene" role="img" aria-label="Ink painting of a blossoming cherry tree beside a snowy mountain"></div>
    </header>
    <div class="backdrop"><div class="backdrop__blossom" role="img" aria-label="Large faint sakura blossom background"></div></div>

    <article class="panel panel--main2">
      <div class="panel__art" role="img" aria-label="Pink sakura flower illustration"></div>
      <div class="panel__icon" style="left:0;top:8px" role="img" aria-label="Bowl of edamame"></div>
      <h2 class="panel__title">Main Dish</h2>
      <ul class="menu menu--compact">
        <li class="menu__row">Japanese Curry (prawn $14)<span class="menu__leader"></span>$12</li>
        <li class="menu__note">(bowl of steamed rice with chicken, pork or prawn<br>&nbsp;with Japanese mild curry sauce)</li>
        <li class="menu__row">KatsuDon<span class="menu__leader"></span>$12</li>
        <li class="menu__note">(bowl of steamed rice topped with a deep-fried pork<br>&nbsp;cutlet &amp; egg with the Japanese special sauce)</li>
        <li class="menu__row">OyakoDon<span class="menu__leader"></span>$12</li>
        <li class="menu__note">(bowl of steamed rice topped with chicken &amp; egg<br>&nbsp;with Japanese special sauce)</li>
        <li class="menu__row">SpiceDon<span class="menu__leader"></span>$12</li>
        <li class="menu__note">(bowl of steamed rice topped with beef or chicken<br>&nbsp;with Japanese spice sauce)</li>
        <li class="menu__row">GingerDon<span class="menu__leader"></span>$12</li>
        <li class="menu__note">(bowl of steamed rice topped with beef or chicken<br>&nbsp;with Japanese ginger sauce)</li>
        <li class="menu__row">Sushi<span class="menu__leader"></span>$3</li>
        <li class="menu__note">(rolled every day with seasonal ingredients)</li>
      </ul>
    </article>

    <article class="panel panel--sweets">
      <div class="panel__art" role="img" aria-label="Pink sakura flower illustration"></div>
      <h2 class="panel__title panel__title--small">Japanese Style Sweets</h2>
      <ul class="menu menu--sweets">
        <li class="menu__row">Black Sesame Ice Cream<span class="menu__leader"></span>$4.5</li>
        <li class="menu__row">Green Tea Ice Cream<span class="menu__leader"></span>$4.5</li>
      </ul>
    </article>
  </section>

</div>
</body>
</html>
```